Letter head to include new logo and the following services:<br/><br/>Static Security, Mobile Patrols, Alarm Response & Key Holding, Alarm & CCTV Monitoring, Welfare Hire.<br/><br/>Phone: 0800 417 3926<br/>E-mail: security@tqv-holdings.co.uk<br/><br/>Southern Office:<br/>TQV Security & Monitoring<br/>2nd Floor<br/>7 Larchmere Close<br/>London<br/>N15 4PW<br/><br/>Northern Office:<br/>TQV Security & Monitoring<br/>Gateway 14 Vehicle Compound<br/>Pelham Street<br/>Aston<br/>Sheffield<br/>S21 7HT<br/><br/>I need the files as PDF and an editable Microsoft Word Document. See attached file from my other business as an example. Do not copy information from uploaded word document, its just an example only. Logo also attached.<br/><br/><br/>SEE OTHER PROJECTS, THEY ARE ALL LINKED<br/> <br/>

```html
<!DOCTYPE html>
<html lang="en">
<head>
<meta charset="utf-8">
<title>TQV Security &amp; Monitoring – Letterhead</title>
<link href="https://fonts.googleapis.com/css2?family=Arimo:wght@400;700&family=Lato:wght@400;700&display=swap" rel="stylesheet">
<style>
  :root {
    --bg: #bcd8f2;
    --paper: #ffffff;
    --brand-blue: #1f6fbf;
    --brand-blue-light: #4a95d8;
    --charcoal: #3c3c3c;
    --body-grey: #6d6d6d;
    --faint-blue: #dbe8f5;
  }
  * { box-sizing: border-box; margin: 0; padding: 0; }
  html, body { width: 1200px; height: 784px; overflow: hidden; }
  body { background: var(--bg); font-family: "Arimo", Arial, sans-serif; }

  .letterhead {
    position: absolute; left: 340px; top: 22px;
    width: 520px; height: 740px;
    background: var(--paper);
    box-shadow: 0 4px 16px rgba(30, 70, 120, .25);
    overflow: hidden;
  }

  /* Header */
  .header-accent { position: absolute; left: 0; top: 0; width: 520px; height: 90px; }
  .brand {
    position: absolute; left: 32px; top: 20px; width: 180px;
    display: flex; align-items: center; gap: 8px;
  }
  .brand-dot { width: 24px; height: 24px; border-radius: 50%; background: var(--brand-blue); flex: none; }
  .brand-name { font-weight: 700; font-size: 15px; line-height: 17px; color: var(--brand-blue); }
  .services {
    position: absolute; right: 22px; top: 38px; width: 280px;
    font-family: "Lato", sans-serif; font-size: 9.5px; line-height: 14px;
    color: var(--charcoal); text-align: right;
  }
  .services .sep { color: var(--brand-blue-light); }

  /* Body */
  .letter-body {
    position: absolute; left: 44px; top: 104px; width: 432px;
    font-size: 8.4px; line-height: 12.4px; color: var(--body-grey);
  }
  .letter-body p { margin-bottom: 12px; }
  .signature {
    position: absolute; left: 64px; top: 402px; width: 170px; height: 54px;
    background: linear-gradient(90deg, #e9e9e9, #f6f6f6);
    border-radius: 4px;
  }
  .watermark {
    position: absolute; left: 226px; top: 540px; width: 118px; height: 118px;
    border-radius: 50%; background: var(--faint-blue);
  }

  /* Footer */
  .footer-accent { position: absolute; left: 0; bottom: 0; width: 520px; height: 130px; }
  .footer-info { position: absolute; left: 30px; bottom: 46px; }
  .footer-name { font-weight: 700; font-size: 11px; color: var(--brand-blue); margin-bottom: 5px; }
  .footer-line {
    display: flex; align-items: center; gap: 4px;
    font-size: 6.4px; line-height: 10px; color: var(--charcoal);
  }
  .footer-line svg { width: 7px; height: 7px; flex: none; }
  .footer-line .gap { width: 6px; }
  .web {
    position: absolute; right: 22px; bottom: 8px;
    font-weight: 700; font-size: 10px; color: #fff;
  }
</style>
</head>
<body>
<main class="letterhead">
  <svg class="header-accent" viewBox="0 0 520 90" aria-hidden="true">
    <rect x="0" y="0" width="70" height="5" fill="#3c3c3c"/>
    <rect x="230" y="70" width="290" height="4" fill="#1f6fbf"/>
    <rect x="30" y="62" width="170" height="1.5" fill="#1f6fbf"/>
  </svg>

  <div class="brand">
    <span class="brand-dot"></span>
    <span class="brand-name">TQV Security<br>&amp; Monitoring</span>
  </div>

  <div class="services">
    Static Security <span class="sep">/</span> Mobile Patrols <span class="sep">/</span> Alarm Response &amp; Key Holding<br>
    Alarm &amp; CCTV Monitoring <span class="sep">/</span> Welfare Hire.
  </div>

  <section class="letter-body">
    <p>Lorem Ipsum is simply dummy text of the printing and typesetting industry. Lorem Ipsum has been the industry's standard dummy text ever since the 1500s, when an unknown printer took a galley of type and scrambled it to make a type specimen book. It has survived not only five centuries, but also the leap into electronic typesetting, remaining essentially unchanged. It was popularised in the 1960s with the release of Linoset sheets containing Lorem Ipsum passages, and more recently with desktop publishing software like Quillset Layout including versions of Lorem Ipsum.</p>
    <p>It is a long established fact that a reader will be distracted by the readable content of a page when looking at its layout. The point of using Lorem Ipsum is that it has a more-or-less normal distribution of letters, as opposed to using 'Content here, content here', making it look like readable English. Many desktop publishing packages and web page editors now use Lorem Ipsum as their default model text, and a search for 'lorem ipsum' will uncover many web sites still in their infancy. Various versions have evolved over the years, sometimes by accident, sometimes on purpose (injected humour and the like).</p>
    <p>Contrary to popular belief, Lorem Ipsum is not simply random text. It has roots in a piece of classical Latin literature from 45 BC, making it over 2000 years old. Harold Penwick, a Latin professor at Ashcombe College in Virginia, looked up one of the more obscure Latin words, consectetur, from a Lorem Ipsum passage, and going through the cites of the word in classical literature, discovered the undoubtable source. Lorem Ipsum comes from sections 1.10.32 and 1.10.33 of "de Finibus Bonorum et Malorum" structures, to generate Lorem Ipsum which looks reasonable. The generated Lorem Ipsum is therefore always free from repetition, injected humour, or non-characteristic words etc.</p>
  </section>

  <div class="signature" role="img" aria-label="Handwritten signature of the sender"></div>
  <div class="watermark" aria-hidden="true"></div>

  <svg class="footer-accent" viewBox="0 0 520 130" aria-hidden="true">
    <rect x="0" y="38" width="6" height="92" fill="#1f6fbf"/>
    <rect x="10" y="46" width="3" height="84" fill="#3c3c3c"/>
    <rect x="30" y="96" width="250" height="1.2" fill="#1f6fbf"/>
    <rect x="30" y="100" width="180" height="1" fill="#3c3c3c"/>
    <polygon points="300,104 520,104 520,130 280,130" fill="#1f6fbf"/>
  </svg>

  <footer class="footer-info">
    <div class="footer-name">TQV Security &amp; Monitoring</div>
    <div class="footer-line">
      <svg viewBox="0 0 10 10"><path d="M5 0a3.5 3.5 0 0 0-3.5 3.5C1.5 6 5 10 5 10s3.5-4 3.5-6.5A3.5 3.5 0 0 0 5 0z" fill="#3c3c3c"/></svg>
      Southern Office : 2nd Floor, 7 Larchmere Close London N15 4PW
      <span class="gap"></span>
      <svg viewBox="0 0 10 10"><path d="M2 1l2 2-1 1.5c.6 1.2 1.3 1.9 2.5 2.5L7 6l2 2-1.5 1.5C4 9 1 6 .5 2.5z" fill="#3c3c3c"/></svg>
      0800 417 3926
      <span class="gap"></span>
      <svg viewBox="0 0 10 10"><rect x=".5" y="2" width="9" height="6" fill="none" stroke="#3c3c3c"/><path d="M.5 2L5 5.5 9.5 2" fill="none" stroke="#3c3c3c"/></svg>
      security@tqv-holdings.co.uk
    </div>
    <div class="footer-line">
      <svg viewBox="0 0 10 10"><path d="M5 0a3.5 3.5 0 0 0-3.5 3.5C1.5 6 5 10 5 10s3.5-4 3.5-6.5A3.5 3.5 0 0 0 5 0z" fill="#3c3c3c"/></svg>
      Northern Office : Gateway 14 Vehicle Compound, Pelham Street, Aston Sheffield S21 7HT
    </div>
  </footer>

  <div class="web">www.tqv-holdings.co.uk</div>
</main>
</body>
</html>
```